Freelance film producer/editor wants you to gleam nova!

'Gleam Nova' is my production business based in Melbourne, though I do a fair bit of work overseas. I'm a one woman show most of the time but enlist other crew members for larger projects. I manage productions from start to finish including producing, filming, editing, distribution, photography and animation.

My current tag line and details are as follows:

Petra Vandoren
Producer. Editor. Thinker.
[M] +61 492 157 630
[E] pv[at]brightpanel.com.au
www.brightpanel.com.au

I have a fairly wicked sense of humour and love a good pun, so feel free to work this into your design!

The final designs should demonstrate the areas I work in but not limited to. I'd rather not use old and typical "film" looking elements such as a clapper or negative reel. Having said that, the logo itself (attached) is quite typical because the first 'o' is a closed aperture and the second is a wide aperture. Happy for the logo to be pulled apart for the business card to be more interesting.

The majority of projects I work on are quite different and in some cases a bit crazy. Lots of travel involved. The main difference between me and other producers is that I don't say I work in 'film', even though i do. I want the card to leave me open to new roles and projects as opposed to squashing myself into one particular category.

I'm open to colour but prefer a simple design that isn't too hectic.

I have also attached an example I did like that was printed on plastic but then I realised so many other people had ripped it off....

I'm open to paper board or plastic (transparent) designs etc. One sided or two sided.

Thanks for sharing your ideas with me and please, go as nuts as you want to with this! :)

Target Market(s)

My clients range from non profits in health and educational institutions to record labels and well known artists. The business attracts corporates as well though the majority of my business is achieved through referral and word of mouth so most people will soon realise that my personality and work are very much intertwined and the reason they hire me for a job.

Industry/Entity Type

Business

Font styles to use
Other font styles liked:
• Eurostile or similar

Requirements
Must have
• I have a very open mind when it comes to design. I do like the existing tag line but if you can come up with something better I'm all ears! (and eyes)

Nice to have
• Back of the business card can be graphics, there can be transparent elements or holes, embossing options...
Should not have
• Besides my name, nothing should scream "I am woman!" because in my industry that's not a selling point.

The colour pink is a definite no.

```html
<!DOCTYPE html>
<html lang="en">
<head>
<meta charset="utf-8">
<title>Petra Vandoren — Business Card</title>
<link rel="stylesheet" href="https://fonts.googleapis.com/css2?family=Noto+Sans+JP:wght@400;500&display=swap">
<style>
  :root {
    --page: #ffffff;
    --card: #333333;
    --window: #fefefe;
    --ink-light: #ffffff;
    --accent-orange: #f0943a;
    --accent-blue: #1f67a3;
  }
  html, body {
    margin: 0;
    padding: 0;
    width: 1200px;
    height: 1000px;
    overflow: hidden;
    background: var(--page);
  }
  .canvas {
    position: relative;
    width: 1200px;
    height: 1000px;
    font-family: "Noto Sans JP", sans-serif;
  }
  .card {
    position: absolute;
    left: 0;
    top: 113px;
    width: 1200px;
    height: 773px;
    background: var(--card);
  }
  .card__window {
    position: absolute;
    left: 82px;
    top: 124px;
    width: 1035px;
    height: 456px;
    background: var(--window);
  }
  .identity {
    position: absolute;
    left: 60px;
    width: 500px;
    top: 618px;
    text-align: center;
  }
  .identity__name {
    margin: 0;
    color: var(--ink-light);
    font-weight: 400;
    font-size: 50px;
    line-height: 64px;
    letter-spacing: 0.5px;
  }
  .identity__tagline {
    margin: 0;
    color: var(--accent-orange);
    font-weight: 400;
    font-size: 33px;
    line-height: 46px;
  }
  .contact {
    position: absolute;
    right: 91px;
    top: 616px;
    text-align: right;
  }
  .contact__phone {
    margin: 0;
    color: var(--ink-light);
    font-weight: 400;
    font-size: 43px;
    line-height: 60px;
    letter-spacing: 0.5px;
  }
  .contact__email {
    margin: 0;
    color: var(--accent-blue);
    font-weight: 400;
    font-size: 42px;
    line-height: 54px;
  }
</style>
</head>
<body>
  <div class="canvas">
    <section class="card">
      <div class="card__window"></div>
      <div class="identity">
        <h1 class="identity__name">Petra Vandoren</h1>
        <p class="identity__tagline">Producer. Editor. Thinker.</p>
      </div>
      <div class="contact">
        <p class="contact__phone">+61 492 157 630</p>
        <p class="contact__email">petra@brightpanel.com.au</p>
      </div>
    </section>
  </div>
</body>
</html>
```